Accounting firm needs a flyer "TREV Partners".. many job after this Stationary, business card

We need a flyer for a new company based in Melbourne Australia. We are group of young professionals who intend to provide various accounting services, taxation, finance, bookkeeping and payroll, Business service service advisory and management consulting.The main task of the firm is to provide accounting and taxation services. we then use our associates/referral partners to assist client with their legal, migration, finance needs.

We would like to see designs that match our logo, business card and letter head which I have uploaded along with this. I have also uploaded some of our website contents that might be used in flyers.
My favorite colors are: Blue (navy and royal blue), Teal (blue green), Turquoise, purple(orchid, lavender, plum).

Our brand:
TREV Partners
Where advice mean more

Our mission:
To group the professionals in house, where advice mean more and turn into better business for our people, for our clients and four our communities.

We like our logo, however we are still not sure about our business card. So if we are open to work with someone who works with flyers and business card at the same time .

Target Market(s)

Individual and business client in Australia

Industry/Entity Type

Finance And Accounting

Colors
0255a3
3176b5
0493ce
33a6d7
886aae
b768aa
00a990
33b8a4

Requirements
Must have
• TREV Partners logo
• Liability limited by a scheme approved under the professional standards legislation
• Our motto: TREV Partners where counsel goes further
• Short description of our services:
• • Bookkeeping & Payroll
• • Finance & Capital Raising
• • Taxation, Accounting and compliances
• • Business service and advisory
• • Migration
• • ASIC and Corporate Secretarial
• • Business law and legal services
• About us
• TREV aim to be more than just an accounting firm. We support our clients to help them achieve their personal and business goals by offering a fully integrated advisory service, helping clients to build wealth and protect their assets.We will bring together the relevant professionals across a number of specialties and locations; providing a responsive, personalised solution.
• Our mission: To group the professionals in house, where advice mean more and turn into better business for our people, for our clients and four our communities.
Nice to have
• Tax agent logo
• NCB logo

```html
<!DOCTYPE html>
<html lang="en">
<head>
<meta charset="utf-8">
<title>TREV Partners – Flyer</title>
<link rel="stylesheet" href="https://fonts.googleapis.com/css2?family=Hind:wght@400;500;600;700&display=swap">
<style>
:root{
  --stage:#222222;
  --navy:#1b2a6b;
  --royal:#0255a3;
  --blue-mid:#3176b5;
  --sky:#33a6d7;
  --plum:#a86aa4;
  --teal:#17a088;
  --ink:#1a1a1a;
  --paper:#ffffff;
  --panel:#eef0f2;
}
*{box-sizing:border-box;margin:0;padding:0}
html,body{width:1200px;height:1000px;overflow:hidden}
body{background:var(--stage);font-family:"Hind",Arial,sans-serif;color:var(--ink)}
.flyer{position:absolute;left:248px;top:43px;width:705px;height:914px;background:var(--paper);overflow:hidden}
.hero{position:absolute;left:0;top:0;width:705px;height:315px;
  background:linear-gradient(160deg,#d9d4cc 0%,#b9a890 35%,#8c7763 60%,#d7d2cb 100%)}
.brand{position:absolute;left:40px;top:60px;display:flex;align-items:center;gap:10px}
.brand-dot{width:34px;height:34px;border-radius:50%;background:var(--royal)}
.brand-name{font-weight:700;font-size:34px;color:var(--royal);letter-spacing:1px}
.badge{position:absolute;border-radius:50%}
.badge-tax{left:518px;top:262px;width:48px;height:48px;background:#f2f2ee;border:3px solid #c9c9c2}
.badge-ncb{left:590px;top:258px;width:40px;height:40px;background:var(--plum)}
.accent-band{position:absolute;left:0;top:315px;width:705px;height:12px;background:var(--plum)}
.intro{position:absolute;left:43px;top:334px;width:622px;font-size:12.4px;line-height:14.4px}
.intro h2{font-size:14.5px;font-weight:600;color:var(--navy);margin-bottom:1px}
.intro p+h2{margin-top:12px}
.intro .values{color:var(--navy);font-weight:600}
.services-bar{position:absolute;left:0;top:480px;width:705px;height:28px;background:var(--teal);
  color:#fff;font-weight:600;font-size:15px;text-align:center;line-height:30px}
.services{position:absolute;left:0;top:508px;width:705px;height:357px;
  background:linear-gradient(180deg,#f3f4f5 0%,#e6e8ea 100%)}
.col{position:absolute;top:15px;width:297px;font-size:12.4px;line-height:14px;text-align:justify}
.col-left{left:43px}.col-right{left:367px}
.service{margin-bottom:13px}
.service h3{display:inline;font-size:12.4px;font-weight:600;color:var(--navy)}
.service h3::before{content:"";display:inline-block;width:6px;height:6px;background:var(--teal);margin:0 4px 1px 4px}
.footer{position:absolute;left:0;top:865px;width:705px;height:49px;background:var(--royal)}
.footer svg{position:absolute;left:0;top:0}
.contact{position:absolute;top:0;height:49px;display:flex;align-items:center;gap:6px;color:#fff;font-weight:600;font-size:15.5px}
.contact-web{left:42px}.contact-mail{left:322px}.contact-phone{left:522px}
</style>
</head>
<body>
<main class="flyer">
  <div class="hero" role="img" aria-label="Photo of a person working on a laptop at a wooden desk with a coffee cup"></div>
  <div class="brand"><span class="brand-dot"></span><span class="brand-name">TREV</span></div>
  <span class="badge badge-tax"></span>
  <span class="badge badge-ncb"></span>
  <div class="accent-band"></div>

  <section class="intro">
    <h2>Our Mission :</h2>
    <p>To group the professionals in house, whereadvice mean more and turn into better business for our people, for our clients and four our communities.</p>
    <h2>Our Firm :</h2>
    <p>As a group of professionals, our firm are available to provide you with high quality accounting, taxation and business advisory whether you are a business owner, family or an individual client.We have a strategic alliance with our referral lawyers, migration agents and mortgage brokers.</p>
    <p class="values">Our core values &nbsp;include expertise, confidentiality, teamwork and commitment.</p>
  </section>

  <div class="services-bar">Our Services :</div>
  <section class="services">
    <div class="col col-left">
      <div class="service"><h3>Bookkeeping &amp; Payroll</h3> Our bookkeeping involves maintaining accurate and updated records of all your business and personal financial activates. We manage your payroll on an ongoing basis, ensuring that all employees are compensated according to their employment agreements.</div>
      <div class="service"><h3>Finance &amp; Capital Raising</h3> We regularly review client portfolios to identify opportunities and refer them to experienced and professional finance brokers to save and assist them with renegotiating a better deal with their current lender or seek out a better loan from a different lender.</div>
      <div class="service"><h3>Taxation, Accounting and Compliances</h3> At TREV experienced tax agent build close working relationships with you to understand your circumstances and develop customised solutions for your personal income tax and corporate tax exposure.</div>
    </div>
    <div class="col col-right">
      <div class="service"><h3>Business Services and Advisory</h3> While we provide peace of mind though takign care of the usual accounting and tax compliance matters, our real value lies in seeking to help you address business challenges and uncover opportunities.</div>
      <div class="service"><h3>Migration</h3> The business Innovation visa or Employer Business Sponsored visa application can be complex with the requirement to submit various business, financial and asset documents.</div>
      <div class="service"><h3>ASIC and Corporate Secretarial</h3> TREV understand that your corporate register, minutes and officeholder information and other secretarial register must kept for the life of the entity. Therefore, we maintain these documents.</div>
      <div class="service"><h3>Business law and legal services</h3> When it comes to business law and legal services, you want to ensure you have a trusted competent legal team to work alongside with your accountants to help you across the broad range of commercial circumstances</div>
    </div>
  </section>

  <footer class="footer">
    <svg width="705" height="49" aria-hidden="true"><polygon points="0,0 258,0 228,49 0,49" fill="#2f9fd8"/></svg>
    <div class="contact contact-web">
      <svg width="12" height="12" viewBox="0 0 12 12" aria-hidden="true"><circle cx="6" cy="6" r="5" fill="none" stroke="#fff" stroke-width="1.2"/><ellipse cx="6" cy="6" rx="2.2" ry="5" fill="none" stroke="#fff" stroke-width="1"/><line x1="1" y1="6" x2="11" y2="6" stroke="#fff"/></svg>
      www.trevpartners.com.au</div>
    <div class="contact contact-mail">
      <svg width="13" height="11" viewBox="0 0 13 11" aria-hidden="true"><rect x="1" y="2" width="11" height="8" fill="none" stroke="#fff" stroke-width="1.2"/><polyline points="1,2 6.5,7 12,2" fill="none" stroke="#fff" stroke-width="1.2"/></svg>
      hello@trevpartners.com.au</div>
    <div class="contact contact-phone">
      <svg width="13" height="13" viewBox="0 0 13 13" aria-hidden="true"><circle cx="6.5" cy="6.5" r="5.6" fill="none" stroke="#fff" stroke-width="1.1"/><path d="M4.5 3.8 l1.2 -.3 .6 1.6 -.8 .6 q.6 1.4 1.9 2 l.6 -.8 1.6 .6 -.3 1.2 q-3.8 .2 -4.8 -4.9z" fill="#fff"/></svg>
      0491 570 156</div>
  </footer>
</main>
</body>
</html>
```